Management Consultancy needs sharp professional services showcased in a brochure

We are a management consultancy specializing on contract management and conflict avoidance services requiring a professional brochure showcasing our services to prospective clients.

Attached are a selection of existing stationary and the colour scheme.

Further details on our company can be found at www.velmor-advisory-partners.com
Updates

Preference is for bi-fold, however, innovative tri-fold will be considered. Added Monday, August 7, 2017

Target Market(s)

Construction companies, consultants, developers, oil and gas service providers, NGO's, SME's.

Industry/Entity Type

Management

Requirements
Must have
• High degree of professionalism with eye catching, sharp detail. No frils.
• Colour scheme as per the attachments
• Font as per attachments - Century Gothic
• Details of our company and services
Nice to have
• Open to ideas, thinking along the lines of a car brochure type design.
• Bi-fold preferred, by trifold accepted if innovative.
Should not have
• Remove reference to the United Arab Emirates.
• No cartoon/clipart photos.

```html
<!DOCTYPE html>
<html lang="en">
<head>
<meta charset="utf-8">
<title>Velmor Advisory – Brochure</title>
<link href="https://fonts.googleapis.com/css2?family=Questrial&display=swap" rel="stylesheet">
<style>
:root{
  --navy:#222d48;
  --navy-deep:#1b2439;
  --red:#c8202a;
  --ink:#4a4a4a;
  --grey-page:#ececec;
  --grey-bg:#bdbdbd;
  --white:#ffffff;
}
*{margin:0;padding:0;box-sizing:border-box}
html,body{width:891px;height:1200px;overflow:hidden}
body{background:var(--grey-bg);font-family:"Questrial",sans-serif;color:var(--ink);position:relative}
.abs{position:absolute}
.spread{position:absolute;left:69px;width:765px;background:var(--white)}
.spread-outer{top:81px;height:495px}
.spread-inner{top:650px;height:494px}
.photo{position:absolute}
.heading{font-size:10px;font-weight:normal;letter-spacing:.2px;color:var(--navy-deep);text-transform:uppercase}
.heading .accent{color:var(--red)}
.body-text{font-size:7.2px;line-height:1.3;text-align:justify}
.body-text p+p{margin-top:7px}
.navy{background:var(--navy);color:var(--white)}
.brand{font-size:19px;font-weight:normal;letter-spacing:.5px;text-transform:uppercase}
.countries{font-size:7px;letter-spacing:.2px;text-transform:uppercase;white-space:nowrap}
.countries .dot{color:var(--red);margin:0 4px}
.footer-line{font-size:7.6px;white-space:nowrap}
.footer-line b{font-weight:normal;color:#fff;letter-spacing:.2px}
.rule{height:1px;background:rgba(255,255,255,.5)}
.sector-list{list-style:none}
.sector-list li{display:flex;align-items:center;gap:9px;font-size:7.6px;line-height:1.05;height:24px}
.sector-list svg{flex:none}
.svc-box{position:absolute;top:289px;width:151px;height:189px;background:#f1f1f1}
.svc-box h3{height:26px;background:var(--navy);color:#fff;font-weight:normal;font-size:9px;letter-spacing:.3px;text-align:center;line-height:26px}
.svc-box .body-text{padding:10px 6px 0 6px}
.svc-list{list-style:none;font-size:7.2px;line-height:1.72;padding:8px 6px 0 6px}
.svc-list li::before{content:"•";color:var(--red);margin-right:3px}
.svc-list .cont{padding-left:6px}
</style>
</head>
<body>

<section class="spread spread-outer">
  <!-- back page -->
  <div class="photo" role="img" aria-label="Greyscale photo of reading glasses and a pen resting on papers on a meeting table" style="left:0;top:0;width:382px;height:164px;background:linear-gradient(160deg,#c9c9c9 0%,#e4e4e4 45%,#9d9d9d 100%)"></div>
  <div class="abs" style="left:14px;top:178px;width:356px">
    <h2 class="heading"><span class="accent">Contact</span> Us</h2>
    <div class="body-text" style="margin-top:10px">
      <p>Velmor Advisory is more than just a professional advisory consultancy; we are an integrated professional team with deep domain expertise, industry knowledge and the ability to work across multiple jurisdictions supported by a wide professional network.</p>
      <p>We forge strong client partnerships and in doing so, we develop and maintain these relationships through performance and delivery of professional services which create and maximise value for our clients.</p>
    </div>
  </div>
  <div class="abs navy" role="img" aria-label="Navy panel with a faint world map" style="left:0;top:291px;width:382px;height:183px;background:radial-gradient(ellipse at 55% 40%,#2f3d62 0%,var(--navy) 55%,var(--navy-deep) 100%)">
    <div class="brand abs" style="left:0;width:382px;top:62px;text-align:center">Velmor Advisory</div>
    <div class="countries abs" style="left:0;width:382px;text-align:center;top:130px">United Kingdom<span class="dot">•</span>Ireland<span class="dot">•</span>Brazil</div>
    <div class="rule abs" style="left:16px;top:145px;width:348px"></div>
    <div class="footer-line abs" style="left:17px;top:152px">Velmor Advisory Limited · E: jhale@velmor-advisory-partners.com · <b>www.velmor-advisory-partners.com</b></div>
  </div>
  <div class="abs" style="left:0;top:474px;width:382px;height:21px;background:var(--grey-page)"></div>

  <!-- cover -->
  <div class="brand abs" style="left:401px;top:62px;color:var(--navy-deep);font-size:17px;white-space:nowrap">Velmor Advisory</div>
  <div class="abs" style="left:560px;top:91px;width:205px;height:8px;background:var(--red)"></div>
  <div class="photo" role="img" aria-label="Greyscale photo of a hand touching a world map with arrows spreading across continents" style="left:382px;top:99px;width:383px;height:299px;background:linear-gradient(135deg,#8f8f8f 0%,#cfcfcf 40%,#a8a8a8 70%,#7a7a7a 100%)"></div>
  <svg class="abs" style="left:382px;top:292px" width="250" height="77" viewBox="0 0 250 77" aria-hidden="true">
    <polygon points="0,0 250,0 200,77 0,77" fill="#e9e9e9" opacity=".93"/>
  </svg>
  <div class="abs" style="left:400px;top:310px;font-size:16px;line-height:1.35;letter-spacing:.3px;color:var(--navy-deep)">THE CONTRACT AND<br>CONFLICT ADVISORY</div>
  <div class="abs navy" style="left:382px;top:398px;width:383px;height:97px;background:linear-gradient(180deg,#26324f,var(--navy-deep))">
    <div class="abs" style="left:0;width:383px;top:43px;text-align:center;font-size:9px">www.velmor-advisory-partners.com</div>
    <div class="countries abs" style="left:0;width:383px;text-align:center;top:75px;font-size:5.6px">United Kingdom<span class="dot">•</span>Ireland<span class="dot">•</span>Brazil</div>
    <div class="rule abs" style="left:56px;top:84px;width:272px"></div>
    <div class="abs" style="left:0;width:383px;text-align:center;top:88px;font-size:5.4px;white-space:nowrap">Velmor Advisory Limited · E: jhale@velmor-advisory-partners.com · www.velmor-advisory-partners.com</div>
  </div>
</section>

<section class="spread spread-inner">
  <div class="photo" role="img" aria-label="Greyscale photo of hands using a tablet at a desk" style="left:0;top:0;width:200px;height:136px;background:linear-gradient(120deg,#d7d7d7 0%,#a9a9a9 60%,#8c8c8c 100%)"></div>
  <svg class="abs" style="left:160px;top:0" width="222" height="136" viewBox="0 0 222 136" aria-hidden="true">
    <polygon points="40,0 222,0 222,136 0,136" fill="#222d48"/>
  </svg>
  <div class="abs" style="left:197px;top:33px;width:168px;color:#fff">
    <div style="font-size:7px;letter-spacing:-.1px">THE CONTRACT AND CONFLICT ADVISORY</div>
    <div class="body-text" style="margin-top:11px;font-size:7.4px;line-height:1.25">Through our unique approach to contract and conflict management, we want the best for our clients to ensure that contract integrity, compliance and performance is maintained with the upmost faith, based around our principles.</div>
  </div>

  <div class="abs" style="left:0;top:136px;width:159px;height:358px;background:var(--grey-page)"></div>
  <div class="abs" style="left:14px;top:158px;width:134px">
    <h2 class="heading"><span class="accent">About</span> Us</h2>
    <div class="body-text" style="margin-top:8px;font-size:7.6px;line-height:1.2">We are an experienced contract and conflict advisory providing global contract performance solutions and conflict management to:</div>
    <ul class="sector-list" style="margin-top:12px">
      <li><svg width="18" height="18" viewBox="0 0 18 18"><circle cx="9" cy="9" r="9" fill="#222d48"/><circle cx="9" cy="9" r="5" fill="none" stroke="#fff" stroke-width="1.2"/><path d="M4 9h10M9 4v10" stroke="#fff" stroke-width="1"/></svg>international development organisations</li>
      <li><svg width="18" height="18" viewBox="0 0 18 18"><circle cx="9" cy="9" r="9" fill="#222d48"/><rect x="5" y="6" width="8" height="7" fill="none" stroke="#fff" stroke-width="1.2"/><path d="M5 9h8" stroke="#fff"/></svg>construction industry</li>
      <li><svg width="18" height="18" viewBox="0 0 18 18"><circle cx="9" cy="9" r="9" fill="#222d48"/><path d="M9 4C7 7 6 9 6 10.5a3 3 0 0 0 6 0C12 9 11 7 9 4z" fill="#fff"/></svg>oil and gas industry</li>
      <li><svg width="18" height="18" viewBox="0 0 18 18"><circle cx="9" cy="9" r="9" fill="#222d48"/><path d="M4.5 7L9 4.5 13.5 7z" fill="#fff"/><path d="M6 8v4M8 8v4M10 8v4M12 8v4" stroke="#fff" stroke-width="1"/><path d="M4.5 13h9" stroke="#fff" stroke-width="1.2"/></svg>government sectors</li>
    </ul>
  </div>
  <div class="abs navy" style="left:0;top:349px;width:159px;height:92px">
    <div class="body-text" style="position:absolute;left:15px;top:29px;width:133px;font-size:7.8px;line-height:1.2">If value, whether financial or relationship is not achieved, then we are not finished, we have only just begun.</div>
  </div>
  <div class="abs" style="left:17px;top:469px;font-size:8.6px;color:var(--navy-deep)">www.velmor-advisory-partners.com</div>

  <div class="abs" style="left:197px;top:158px;width:167px">
    <h2 class="heading"><span class="accent">Whay</span> Choose Us</h2>
    <div class="body-text" style="margin-top:10px">
      <p>Observing the standard of consultancy services and magnitude of contractual engagements and conflicts, we see the opportunity to make things better, better engagements, better awareness, better performance, which all lead to better value in terms of financial benefit and relationship maintenance.</p>
      <p>We firmly believe in party success in a non litigious environment.</p>
      <p>Our services are uniquely delivered through our integrated management consultancy model, with a single point of contact and responsibility, and focused attention to detail.</p>
      <p>We provide advisory services and solutions resolving past and current claims, and in doing so, preparing our clients for a conflict free future based on our core principles of integrity, equality and strength, ensuring compliance and experience at an intimate professional level.</p>
      <p>We aim to have our clients feel our principles in our presence and in our advisories, giving the service which is deserved.</p>
    </div>
  </div>

  <div class="photo" role="img" aria-label="Greyscale photo of business people shaking hands in a meeting" style="left:382px;top:0;width:383px;height:136px;background:linear-gradient(100deg,#c4c4c4 0%,#8d8d8d 35%,#6f6f6f 60%,#b5b5b5 100%)"></div>
  <div class="abs" style="left:382px;top:136px;width:383px;height:358px;background:linear-gradient(180deg,#e3e3e3,#f4f4f4 40%,#ffffff)"></div>
  <div class="abs" style="left:400px;top:158px;width:349px">
    <h2 class="heading"><span class="accent">Our</span> Services</h2>
    <div class="body-text" style="margin-top:10px">Every contract has at least two parties; every party has a goal, and every goal matters. Each party must work in equilibrium as a contractual partnership or alliance, it is on this premise we aim to deliver truly mutual agreements, maintaining the contract integrity from inception through the contract life, and where we are not party to the original agreement, we provide effective solutions to contractual conflict via our unique mediation methodology at all positions of the conflict cycle and aim to enhance all aspects of contract performance by effective audit and management.</div>
  </div>

  <div class="svc-box" style="left:400px">
    <h3>CONFLICT ADVISORY</h3>
    <div class="body-text">Every conflict has the ability to be settled, it is on this premise we deliver effective solutions to contractual and commercial disputes with the aim of preserving the relationships and strengthening the parties for the future ahead.</div>
    <ul class="svc-list">
      <li>Restoration and Mediation Services</li>
      <li>Shuttle Diplomacy Services and In<br><span class="cont">Persona Intermediary Services</span></li>
      <li>Negotiation Support Services</li>
      <li>Workplace Mediation Services</li>
    </ul>
  </div>
  <div class="svc-box" style="left:581px">
    <h3>CONTRACT ADVISORY</h3>
    <div class="body-text">Through review, planning and effective application, we ensure that contractual obligations are maintained and risks are mitigated through the full contract life cycle providing the optimum contractual engagement.</div>
    <ul class="svc-list">
      <li>Contract Troubleshooting</li>
      <li>Contracts Audit Services and<br><span class="cont">Performance Management</span></li>
      <li>Strategic Review &amp; Risk Assessment</li>
      <li>Contract Fraud Investigation</li>
    </ul>
  </div>
</section>

</body>
</html>
```